Brochure Design Project

Check our www.harbourlanehomes.example. Company Name is "Harbour Lane Living" and the brochure is to be named "Golden Tides Ahead".

We are seeking a brochure that captures the essence of the idea of living aboard a cruise ship in retirement therefore must encompass not only cruising but also retirement living, therefore we're promoting "a lifestyle better than living ashore in a retirement village".

Brochure will be around 20+ pages though there will only most likely only be around 6 pages of actual templates needed which can be used interchangeably plus a front and back cover.

Some pictures on the brochure will take up full pages with maybe a caption so these other pages should be pretty quick.

Must have great presence and "feel" about it.

Friendly, cheery brochure with bright colours.

Must "look a million dollars" as the market we're targeting is very selective and we're competing in a very competitive market, retirement villages where our clientele is investing large sums of money in their retirement and they are basing their decision on whether to trust us on possibly only this brochure.

This is a new project that will launch on television, radio, pamphlet and brochure in the next 6 weeks.

Work on a brochure I'd been doing attached. Don't just want a repeat of this brochure. This is to provide you with various pieces of text to start the brochure, not to copy the design, which I think is antique and needs completely redoing.

Project Deadline Extended
Reason: At present we have only received a few designs and at present none of them are truly suitable to what we're after or require quite a few changes in terms of creativity to even come close to what we'd be expecting from professional graphic designers.

Project Deadline Extended
Reason: New designers have accepted the invitation to submit designs and many have only had a couple of days to submit designs.

If you haven't already submitted your final designs, please finalise and submit them. Deadline is almost reached.

We look forward to the seeing the final submissions.

Regards,

Harbour Lane Living Ltd.

50+ age bracket (therefore larger writing for brochure text)

Radio

Must have
• We are after classy and sophisticated, not gaudy and cheap so the design must look formal yet modern and eschew the virtues of contemporary and exotic and a higher standard of retirement living rather than "bright, gaudy, cheap and a quick buck".

Our company is designed to provide sophisticated and practical living arrangements for people that are looking for comfortable, practical yet stylishly different in terms of the elegance and lifestyle that people would normally expect for the price of standard living arrangements.

Brochure when completed must be sent in an editable format rather than just static.

Must have a section for pricing comparison between costs of living in "Own Home vs. Retirement Village vs. Harbour Lane Living" for comparision of costs.

Must also have a second comparison with the same titles though this is a "Features/Facilities Comparison".

Must use only royalty-free photography.

Must NOT use pictures of GIANT cruise ships. The ships we're providing our clientelle are mid-1990's ships therefore have a capacity of around 800-1000 capacity, not like today's MEGA-liners that hold 2000-5000 passengers. We don't want to mislead our clientele.

Must NOT use pictures of ships with any names or logos on them (to forestall the possibility of copyright and trademark infringement).

```html
<!DOCTYPE html>
<html lang="en">
<head>
<meta charset="utf-8">
<title>Golden Tides Ahead – Onboard Facilities</title>
<link href="https://fonts.googleapis.com/css2?family=Lora:ital,wght@0,400;0,600;1,400&family=Playfair+Display:ital,wght@0,600;1,500&family=Lato:wght@400;700&display=swap" rel="stylesheet">
<style>
  :root {
    --ocean: #0b7a99;
    --ocean-deep: #0a4f6b;
    --lagoon: #e3f4f7;
    --coral: #ef6a55;
    --sun: #f4b63f;
    --sand: #fffaf2;
    --ink: #23333d;
    --muted: #5d6f78;
    --white: #ffffff;
  }
  * { margin: 0; padding: 0; box-sizing: border-box; }
  html, body { width: 1200px; height: 777px; overflow: hidden; background: var(--white); }
  .spread { display: flex; width: 1200px; height: 777px; color: var(--ink); font-family: "Lora", Georgia, serif; }

  .page-left {
    position: relative; width: 600px; height: 777px; background: var(--sand);
    padding: 34px 48px 0 48px; display: flex; flex-direction: column;
  }
  .page-left::before {
    content: ""; position: absolute; left: 0; top: 0; width: 600px; height: 8px;
    background: linear-gradient(90deg, var(--ocean) 0%, var(--ocean) 60%, var(--sun) 60%, var(--sun) 80%, var(--coral) 80%);
  }

  .kicker { font-family: "Lato", Arial, sans-serif; font-weight: 700; font-size: 11px; letter-spacing: 3px; text-transform: uppercase; color: var(--coral); height: 16px; }
  .page-title { font-family: "Playfair Display", Georgia, serif; font-weight: 600; font-size: 32px; line-height: 42px; color: var(--ocean-deep); }
  .title-rule { width: 72px; height: 3px; background: var(--sun); margin: 6px 0 12px; border-radius: 2px; }

  .intro { font-size: 13px; line-height: 18.5px; color: var(--ink); }
  .intro em { color: var(--ocean); font-style: italic; }

  .facilities {
    margin-top: 16px; background: var(--lagoon); border-left: 4px solid var(--ocean);
    border-radius: 0 10px 10px 0; padding: 14px 20px 14px 22px;
  }
  .facilities h2 { font-family: "Playfair Display", Georgia, serif; font-style: italic; font-weight: 500; font-size: 21px; line-height: 28px; color: var(--coral); margin-bottom: 6px; }
  .facility-grid { list-style: none; display: grid; grid-template-columns: repeat(3, 1fr); grid-auto-rows: 25px; column-gap: 10px; }
  .facility-grid li { display: flex; align-items: center; font-family: "Lato", Arial, sans-serif; font-size: 13px; color: var(--ink); white-space: nowrap; }
  .facility-grid svg { width: 16px; height: 16px; margin-right: 9px; flex: none; }

  .photo-row { display: flex; gap: 14px; margin-top: 16px; }
  .photo { height: 140px; border-radius: 10px; flex: 1; }
  .photo-gym { background: linear-gradient(160deg, #a9d3e3 0%, #6fa9bf 40%, #3e5f6c 75%, #28363d 100%); }
  .photo-promenade { background: linear-gradient(180deg, #f1b9c9 0%, #d98bb0 35%, #a8679a 65%, #5c3a66 100%); }

  .page-footer {
    position: absolute; left: 48px; right: 48px; bottom: 22px; height: 18px;
    display: flex; align-items: center; gap: 14px;
    font-family: "Lato", Arial, sans-serif; font-size: 9.5px; color: var(--muted);
  }
  .page-number { flex: none; width: 30px; height: 18px; border-radius: 9px; background: var(--ocean); color: var(--white); font-weight: 700; font-size: 10px; display: flex; align-items: center; justify-content: center; }

  .page-right {
    width: 600px; height: 777px;
    background:
      radial-gradient(ellipse at 75% 40%, rgba(150,225,245,0.75) 0%, transparent 35%),
      radial-gradient(ellipse at 35% 50%, rgba(120,215,235,0.6) 0%, transparent 40%),
      radial-gradient(ellipse at 55% 85%, rgba(60,200,140,0.7) 0%, transparent 45%),
      linear-gradient(180deg, #0f2a3d 0%, #1b5577 25%, #2584a6 55%, #176a63 80%, #0d2c33 100%);
  }
</style>
</head>
<body>
<main class="spread">
  <section class="page-left">
    <p class="kicker">Onboard Facilities</p>
    <h1 class="page-title">We thought of everything.</h1>
    <div class="title-rule"></div>

    <p class="intro"><em>The facilities on-board the Harbour Lane Living International Limited ships are fantastic and you’ll have everything you need.</em> There will always be plenty to do on board your Harbour Lane Living cruise ship. Aside from the side trips and visits on shore at a plethora of different and exotic destinations every year, you will also have the opportunity to get the most out of the cruise ship itself. The Harbour Lane Living ships are fitted with everything you’ll need to keep fit, party the night away, relax and play cards, get a massage, have a swim, play the pokies or just relax and have a barbeque with friends. In comparison to a retirement village where unless you spend a small fortune, you’d have a games room and some old newspapers, with the Harbour Lane Living cruise ships you’ll have all of the facilities much the same as staying in a 5-star hotel.</p>

    <div class="facilities">
      <h2>What kind of facilities are there?</h2>
      <ul class="facility-grid">
        <li><svg viewBox="0 0 16 16"><circle cx="8" cy="8" r="8" fill="var(--sun)"/><path d="M4.5 8.3l2.3 2.3 4.7-4.9" fill="none" stroke="#fff" stroke-width="1.8" stroke-linecap="round" stroke-linejoin="round"/></svg>Restaurants &amp; Bars</li>
        <li><svg viewBox="0 0 16 16"><circle cx="8" cy="8" r="8" fill="var(--sun)"/><path d="M4.5 8.3l2.3 2.3 4.7-4.9" fill="none" stroke="#fff" stroke-width="1.8" stroke-linecap="round" stroke-linejoin="round"/></svg>Sauna</li>
        <li><svg viewBox="0 0 16 16"><circle cx="8" cy="8" r="8" fill="var(--sun)"/><path d="M4.5 8.3l2.3 2.3 4.7-4.9" fill="none" stroke="#fff" stroke-width="1.8" stroke-linecap="round" stroke-linejoin="round"/></svg>Swimming Pool</li>
        <li><svg viewBox="0 0 16 16"><circle cx="8" cy="8" r="8" fill="var(--sun)"/><path d="M4.5 8.3l2.3 2.3 4.7-4.9" fill="none" stroke="#fff" stroke-width="1.8" stroke-linecap="round" stroke-linejoin="round"/></svg>Show Lounge</li>
        <li><svg viewBox="0 0 16 16"><circle cx="8" cy="8" r="8" fill="var(--sun)"/><path d="M4.5 8.3l2.3 2.3 4.7-4.9" fill="none" stroke="#fff" stroke-width="1.8" stroke-linecap="round" stroke-linejoin="round"/></svg>Chapel</li>
        <li><svg viewBox="0 0 16 16"><circle cx="8" cy="8" r="8" fill="var(--sun)"/><path d="M4.5 8.3l2.3 2.3 4.7-4.9" fill="none" stroke="#fff" stroke-width="1.8" stroke-linecap="round" stroke-linejoin="round"/></svg>Poolside Barbeque</li>
        <li><svg viewBox="0 0 16 16"><circle cx="8" cy="8" r="8" fill="var(--sun)"/><path d="M4.5 8.3l2.3 2.3 4.7-4.9" fill="none" stroke="#fff" stroke-width="1.8" stroke-linecap="round" stroke-linejoin="round"/></svg>Captains Club</li>
        <li><svg viewBox="0 0 16 16"><circle cx="8" cy="8" r="8" fill="var(--sun)"/><path d="M4.5 8.3l2.3 2.3 4.7-4.9" fill="none" stroke="#fff" stroke-width="1.8" stroke-linecap="round" stroke-linejoin="round"/></svg>Internet Café</li>
        <li><svg viewBox="0 0 16 16"><circle cx="8" cy="8" r="8" fill="var(--sun)"/><path d="M4.5 8.3l2.3 2.3 4.7-4.9" fill="none" stroke="#fff" stroke-width="1.8" stroke-linecap="round" stroke-linejoin="round"/></svg>Auditorium</li>
        <li><svg viewBox="0 0 16 16"><circle cx="8" cy="8" r="8" fill="var(--sun)"/><path d="M4.5 8.3l2.3 2.3 4.7-4.9" fill="none" stroke="#fff" stroke-width="1.8" stroke-linecap="round" stroke-linejoin="round"/></svg>Library</li>
        <li><svg viewBox="0 0 16 16"><circle cx="8" cy="8" r="8" fill="var(--sun)"/><path d="M4.5 8.3l2.3 2.3 4.7-4.9" fill="none" stroke="#fff" stroke-width="1.8" stroke-linecap="round" stroke-linejoin="round"/></svg>Boutique Shops</li>
        <li><svg viewBox="0 0 16 16"><circle cx="8" cy="8" r="8" fill="var(--sun)"/><path d="M4.5 8.3l2.3 2.3 4.7-4.9" fill="none" stroke="#fff" stroke-width="1.8" stroke-linecap="round" stroke-linejoin="round"/></svg>Fitness Center</li>
        <li><svg viewBox="0 0 16 16"><circle cx="8" cy="8" r="8" fill="var(--sun)"/><path d="M4.5 8.3l2.3 2.3 4.7-4.9" fill="none" stroke="#fff" stroke-width="1.8" stroke-linecap="round" stroke-linejoin="round"/></svg>Night Club</li>
        <li><svg viewBox="0 0 16 16"><circle cx="8" cy="8" r="8" fill="var(--sun)"/><path d="M4.5 8.3l2.3 2.3 4.7-4.9" fill="none" stroke="#fff" stroke-width="1.8" stroke-linecap="round" stroke-linejoin="round"/></svg>Photo Shop</li>
        <li><svg viewBox="0 0 16 16"><circle cx="8" cy="8" r="8" fill="var(--sun)"/><path d="M4.5 8.3l2.3 2.3 4.7-4.9" fill="none" stroke="#fff" stroke-width="1.8" stroke-linecap="round" stroke-linejoin="round"/></svg>Medical Center</li>
        <li><svg viewBox="0 0 16 16"><circle cx="8" cy="8" r="8" fill="var(--sun)"/><path d="M4.5 8.3l2.3 2.3 4.7-4.9" fill="none" stroke="#fff" stroke-width="1.8" stroke-linecap="round" stroke-linejoin="round"/></svg>Beauty Salon</li>
        <li><svg viewBox="0 0 16 16"><circle cx="8" cy="8" r="8" fill="var(--sun)"/><path d="M4.5 8.3l2.3 2.3 4.7-4.9" fill="none" stroke="#fff" stroke-width="1.8" stroke-linecap="round" stroke-linejoin="round"/></svg>Casino</li>
        <li><svg viewBox="0 0 16 16"><circle cx="8" cy="8" r="8" fill="var(--sun)"/><path d="M4.5 8.3l2.3 2.3 4.7-4.9" fill="none" stroke="#fff" stroke-width="1.8" stroke-linecap="round" stroke-linejoin="round"/></svg>Pharmacy</li>
      </ul>
    </div>

    <div class="photo-row">
      <div class="photo photo-gym" role="img" aria-label="Onboard fitness centre with treadmills facing windows over the sea and coastline"></div>
      <div class="photo photo-promenade" role="img" aria-label="Ship's interior promenade with shops, lights and hanging decorations"></div>
    </div>

    <footer class="page-footer">
      <span class="page-number">7</span>
      <span>Copyright© 2013 Harbour Lane Living Ltd. Intellectual property of Harbour Lane Living Ltd. All rights reserved.</span>
    </footer>
  </section>

  <section class="page-right" role="img" aria-label="Full-page photograph of an onboard theatre show: a performer in a leafy costume on a misty stage lit in blue and green, with a jungle backdrop"></section>
</main>
</body>
</html>
```